Natural Light/Organic/Documentary Photography Business

I like a simple, approachable, feminine, earthy/organic feel. Earth/neutral tones, nothing too loud or obnoxious. I like the watercolor look. I don't want anything too trendy or something I'll get tired of after a couple months. As far as colors, I am much more a fan of cream/taupe/blue/green...not a fan of pink or purple at all.

Target Market(s)

Weddings & Families

Industry/Entity Type

Wedding Photography

Contact Information for Business Card

website, email, phone number

Font styles to use
Other font styles liked:
• Horizontes, Gotham

Colors

Designer to choose colors to be used in the design.

Requirements
Must have
• Website: www.elspethmarlowe.com
• Phone: 412.638.9057
• Email: elspeth@elspethmarlowe.com
Nice to have
• I like the watercolor look but its not necessary. I like simple/earthy tones. Nothing too loud or distracting. Simple & feminine without being too girly. I like an approachable/soft feel.
• Instagram: www.instagram.com/elspethmarlowephotography/
Should not have
• NO loud colors or design or pattern. I do not want a photo of a camera or lens or anything cheesy like that.

```html
<!DOCTYPE html>
<html lang="en">
<head>
<meta charset="utf-8">
<title>Elspeth Marlowe Photography – Business Card</title>
<link rel="stylesheet" href="https://fonts.googleapis.com/css2?family=Lato:wght@300;400&family=Source+Code+Pro:wght@400&display=swap">
<style>
  :root {
    --ink: #5f5c5a;
    --ink-soft: #6a6765;
    --wash-green: #b7d6ae;
    --wash-lime: #dfe6a8;
    --wash-violet: #a9a8d6;
    --wash-blue: #c6dcf1;
    --wash-aqua: #cfeef0;
    --wash-pale: #eef3fb;
  }
  html, body {
    margin: 0;
    padding: 0;
    width: 1200px;
    height: 687px;
    overflow: hidden;
    background: #ffffff;
  }
  .card {
    position: relative;
    width: 1200px;
    height: 687px;
    overflow: hidden;
    font-family: "Lato", Arial, sans-serif;
    color: var(--ink);
  }
  .watercolor-wash {
    position: absolute;
    inset: 0;
    background:
      radial-gradient(ellipse 420px 260px at 120px 40px, var(--wash-green) 0%, rgba(183,214,174,0) 100%),
      radial-gradient(ellipse 360px 220px at 900px 20px, var(--wash-lime) 0%, rgba(223,230,168,0) 100%),
      radial-gradient(ellipse 380px 300px at 1120px 200px, var(--wash-violet) 0%, rgba(169,168,214,0) 100%),
      radial-gradient(ellipse 520px 280px at 450px 200px, var(--wash-blue) 0%, rgba(198,220,241,0) 100%),
      radial-gradient(ellipse 380px 240px at 1000px 420px, var(--wash-aqua) 0%, rgba(207,238,240,0) 100%),
      radial-gradient(ellipse 300px 260px at 60px 360px, #d3e2f4 0%, rgba(211,226,244,0) 100%),
      linear-gradient(180deg, #d8e6f4 0%, var(--wash-pale) 70%, #f2f5fc 100%);
  }
  .brand {
    position: absolute;
    left: 0;
    right: 0;
    top: 128px;
    text-align: center;
  }
  .brand-name {
    margin: 0;
    font-weight: 300;
    font-size: 64px;
    letter-spacing: 2px;
    line-height: 1;
    color: var(--ink);
  }
  .brand-tagline {
    margin: 18px 0 0 0;
    font-weight: 400;
    font-size: 16px;
    letter-spacing: 7px;
    padding-left: 7px;
    color: var(--ink-soft);
  }
  .contact {
    position: absolute;
    left: 0;
    right: 0;
    top: 374px;
    text-align: center;
  }
  .contact-phone {
    margin: 0;
    font-weight: 300;
    font-size: 44px;
    line-height: 1;
    letter-spacing: 0.5px;
  }
  .contact-line {
    margin: 0;
    font-family: "Source Code Pro", "Courier New", monospace;
    font-size: 27px;
    line-height: 1;
    color: var(--ink);
  }
  .contact-email { margin-top: 30px; }
  .contact-web { margin-top: 25px; padding-left: 4px; }
</style>
</head>
<body>
  <div class="card">
    <div class="watercolor-wash" role="img" aria-label="Soft watercolor wash background in green, pale yellow, lavender and sky blue tones"></div>

    <header class="brand">
      <h1 class="brand-name">Elspeth Marlowe</h1>
      <p class="brand-tagline">PHOTOGRAPHY</p>
    </header>

    <section class="contact">
      <p class="contact-phone">CELL: 412 - 638 - 9057</p>
      <p class="contact-line contact-email">Email: elspeth@elspethmarlowe.com</p>
      <p class="contact-line contact-web">Info: www.elspethmarlowe.com</p>
    </section>
  </div>
</body>
</html>
```